Search Fund needs a PowerPoint template design

We need a eye-catching and compelling PowerPoint design for a new company based in Chicago called Tarn Ridge Partners. We are search fund with a primary mission to acquire a founder/family/entrepreneur owned businesses (This is similar to a Private Equity firm). Our goal is to offer investors a unique avenue to invest in an attractive business acquisition while providing business owners with an alternative path to exit. We would like the design to reflect crisp and professional nature that many financial firms present. The template should build on the design of the logo including expanding a logical color palette. The presentation will be used to describe facts regarding the firm, financial data and key messaging that we want our investors and potential partners to takeaway.

Target Market(s)

Financial Investors

Industry/Entity Type

Finance

Font styles to use
Serif
Sans Serif

Colors

Designer to choose colors to be used in the design.

Requirements
Must have
• Should include cover page and slide examples. Attractive data displays (graphs, charts, infographics etc.); Compelling cover; fly pages to put in between sections; table of contents page. Needs to have white space to add text.
Should not have
• Do not redesign the logo or change the logo colors. Additional colors should be added to the PowerPoint template

```html
<!DOCTYPE html>
<html lang="en">
<head>
<meta charset="utf-8">
<title>Tarn Ridge Partners – Presentation Template</title>
<link rel="stylesheet" href="https://fonts.googleapis.com/css2?family=Lato:wght@400;700;900&family=Cinzel:wght@400;600&display=swap">
<style>
  :root{
    --blue:#1272c2;
    --blue-deep:#1a4fa0;
    --grey:#9a9a9a;
    --grey-mid:#b4b4b4;
    --ink:#5c5c5c;
    --orange:#ee7d2f;
    --stage:#cfcdcd;
    --paper:#ffffff;
  }
  *{box-sizing:border-box;margin:0;padding:0}
  html,body{width:1200px;height:1200px;overflow:hidden;background:var(--stage);font-family:"Lato",sans-serif}
  .board{position:relative;width:1200px;height:1200px}
  .slide{position:absolute;width:440px;height:330px;background:var(--paper);overflow:hidden;transform-origin:0 0;color:var(--ink)}
  .slide svg.frame{position:absolute;inset:0;width:440px;height:330px}
  .photo{position:absolute}
  .brand{position:absolute;font-weight:900;color:var(--blue);letter-spacing:.5px;white-space:nowrap}
  .cover-photo{left:0;top:0;width:440px;height:330px;background:linear-gradient(160deg,#f6f7f8 0%,#e4e7ea 45%,#eef0f2 70%,#f7f8f9 100%)}
  .cover .brand{left:16px;top:24px;font-size:22px}
  .cover .brand-rule{position:absolute;left:16px;top:56px;width:262px;height:1px;background:var(--grey)}
  .cover-title{position:absolute;left:16px;top:178px;font-size:24px;font-weight:900;color:var(--blue)}
  .url{position:absolute;font-size:6.5px;font-weight:700;letter-spacing:.6px;color:#fff}
  .cover .url{right:16px;bottom:9px}
  .content{background:linear-gradient(180deg,#f1f3f5 0%,#fff 40%,#fff 100%)}
  .slide-head{position:absolute;left:22px;top:14px;font-size:19px;font-weight:900;color:var(--blue);display:flex;align-items:center;gap:10px}
  .slide-head::after{content:"";width:75px;height:1.5px;background:var(--grey)}
  .content .url{right:13px;bottom:8px}
  .page-no{position:absolute;left:10px;bottom:6px;font-size:9px;font-weight:700;color:#fff}
  .body{position:absolute;font-size:8.3px;line-height:13.2px;text-align:justify;color:#6a6a6a}
  .about-photo{left:225px;top:137px;width:200px;height:140px;border:1px solid #ccc;background:linear-gradient(135deg,#d9e4ee,#f3f1ee 50%,#b9c8d6)}
  .chart{position:absolute;left:20px;top:116px;width:405px;height:162px;border:1px solid #ddd;background:#fff}
  .subs{position:absolute;left:20px;top:66px;width:405px;display:grid;grid-template-columns:1fr 1fr;column-gap:30px;row-gap:12px}
  .sub h3{font-size:9px;font-weight:700;color:var(--blue);margin-bottom:2px}
  .sub p{font-size:8.3px;line-height:13px;color:#6a6a6a}
  .hex-label{position:absolute;font-size:7px;line-height:8px;color:#777}
  .hex-label b{display:block;font-size:8px;color:var(--blue);margin-bottom:3px}
  .hex-label.muted b{color:#999}
  .closing-photo{left:0;top:0;width:440px;height:330px;background:radial-gradient(ellipse at 30% 70%,#4a4f57 0%,#2d3036 55%,#1f2125 100%)}
  .closing .brand{left:0;right:0;top:78px;text-align:center;color:#fff;font-size:23px}
  .closing .brand-rule{position:absolute;left:80px;right:80px;top:110px;height:1px;background:rgba(255,255,255,.7)}
  .thanks{position:absolute;left:0;right:0;top:150px;text-align:center;font-family:"Cinzel",serif;color:#fff;font-size:32px;line-height:34px}
  .thanks small{display:block;font-size:16px;line-height:20px}
  .contact{position:absolute;left:0;right:0;text-align:center;font-size:7px;color:#eee}
  .contact svg{width:7px;height:7px;vertical-align:-1px;margin:0 2px 0 8px}
</style>
</head>
<body>
<main class="board">

  <!-- Hero cover -->
  <section class="slide cover" style="left:346px;top:86px;transform:scale(1.2)">
    <div class="photo cover-photo" role="img" aria-label="Soft faded photo of a keyboard and calculator on a desk"></div>
    <svg class="frame" viewBox="0 0 440 330">
      <polygon points="288,0 305,0 418,262 440,250 440,258 410,276" fill="#a9a9a9"/>
      <polygon points="305,0 440,0 440,250 418,262" fill="var(--blue)"/>
      <polygon points="265,330 420,232 440,222 440,330" fill="#a9a9a9"/>
      <polygon points="285,330 440,236 440,330" fill="var(--blue)"/>
      <polygon points="410,276 440,258 440,262 414,278" fill="var(--blue-deep)"/>
    </svg>
    <div class="brand">TARN RIDGE PARTNERS</div>
    <div class="brand-rule"></div>
    <h1 class="cover-title">PRESENTATION TITLE</h1>
    <div class="url">www.tarnridgepartners.com</div>
  </section>

  <!-- 1 cover -->
  <section class="slide cover" style="left:50px;top:581px;transform:scale(.8)">
    <div class="photo cover-photo" role="img" aria-label="Soft faded photo of a keyboard and calculator on a desk"></div>
    <svg class="frame" viewBox="0 0 440 330">
      <polygon points="288,0 305,0 418,262 440,250 440,258 410,276" fill="#a9a9a9"/>
      <polygon points="305,0 440,0 440,250 418,262" fill="var(--blue)"/>
      <polygon points="265,330 420,232 440,222 440,330" fill="#a9a9a9"/>
      <polygon points="285,330 440,236 440,330" fill="var(--blue)"/>
    </svg>
    <div class="brand">TARN RIDGE PARTNERS</div>
    <div class="brand-rule"></div>
    <h2 class="cover-title">PRESENTATION TITLE</h2>
    <div class="url">www.tarnridgepartners.com</div>
  </section>

  <!-- 2 about -->
  <section class="slide content" style="left:426px;top:579px;transform:scale(.8)">
    <h2 class="slide-head">ABOUT US</h2>
    <p class="body" style="left:20px;top:52px;width:400px">Lorem ipsum dolor sit amet, consectetuer adipiscing elit, sed diam nonummy nibh euismod tincidunt ut laoreet dolore magna aliquam erat volutpat. Ut wisi enim ad minim veniam, quis nostrud exerci tation ullamcoper suscipit lobortis nisl ut aliquip ex ea commodo consequat. Duis autem vel eum iriure dolor in hendrerit in vulputate velit esse molestie consequat, vel illum dolore eu feugiat nulla facilisis.</p>
    <p class="body" style="left:20px;top:136px;width:194px">Lorem ipsum dolor sit amet, consectetuer adipiscing elit, sed diam nonummy nibh euismod tincidunt ut laoreet dolore magna aliquam erat volutpat. Ut wisi enim ad minim veniam, quis nostrud exerci tation ullamcoper suscipit lobortis nisl ut aliquip ex ea commodo consequat. Duis autem vel eum iriure dolor in hendrerit in vulputate velit esse molestie consequat, vel illum dolore eu feugiat nulla facilisis.eum iriure dolor in hendrerit in vulputate.</p>
    <div class="photo about-photo" role="img" aria-label="Photo of three colleagues reviewing a document together"></div>
    <svg class="frame" viewBox="0 0 440 330"><polygon points="0,299 150,320 440,298 440,330 0,330" fill="var(--blue)"/><polyline points="0,296 150,317 440,295" fill="none" stroke="#bbb"/></svg>
    <div class="page-no">2.</div><div class="url">www.tarnridgepartners.com</div>
  </section>

  <!-- 3 chart -->
  <section class="slide content" style="left:800px;top:579px;transform:scale(.8)">
    <h2 class="slide-head">LOREM IPSUM</h2>
    <p class="body" style="left:20px;top:52px;width:400px">Lorem ipsum dolor sit amet, consectetuer adipiscing elit, sed diam nonummy nibh euismod tincidunt ut laoreet dolore magna aliquam erat volutpat. Ut wisi enim ad minim veniam, quis nostrud exerci tation ullamcoper suscipit lobortis nisl ut aliquip ex ea commodo consequat. Duis autem vel eum iriure dolor in hendrerit in vulputate velit esse molestie.</p>
    <svg class="chart" viewBox="0 0 405 162">
      <g font-size="4" fill="#777" font-family="Lato,sans-serif">
        <g stroke="#eee"><line x1="100" y1="140" x2="370" y2="140"/><line x1="100" y1="124" x2="370" y2="124"/><line x1="100" y1="108" x2="370" y2="108"/><line x1="100" y1="92" x2="370" y2="92"/><line x1="100" y1="76" x2="370" y2="76"/><line x1="100" y1="60" x2="370" y2="60"/><line x1="100" y1="44" x2="370" y2="44"/><line x1="100" y1="28" x2="370" y2="28"/><line x1="100" y1="12" x2="370" y2="12"/></g>
        <text x="84" y="127">200</text><text x="84" y="111">400</text><text x="84" y="95">600</text><text x="84" y="79">800</text><text x="80" y="63">1,000</text><text x="80" y="47">1,200</text><text x="80" y="31">1,400</text><text x="80" y="15">1,600</text>
        <text transform="translate(70 105) rotate(-90)">Number of Sources</text>
        <g><rect x="114" y="58" width="7" height="82" fill="var(--blue)"/><rect x="121" y="68" width="7" height="72" fill="var(--orange)"/><rect x="128" y="34" width="7" height="106" fill="var(--grey-mid)"/><text x="116" y="148">2012</text></g>
        <g><rect x="174" y="60" width="7" height="80" fill="var(--blue)"/><rect x="181" y="52" width="7" height="88" fill="var(--orange)"/><rect x="188" y="43" width="7" height="97" fill="var(--grey-mid)"/><text x="176" y="148">2013</text></g>
        <g><rect x="234" y="56" width="7" height="84" fill="var(--blue)"/><rect x="241" y="42" width="7" height="98" fill="var(--orange)"/><rect x="248" y="58" width="7" height="82" fill="var(--grey-mid)"/><text x="236" y="148">2014</text></g>
        <g><rect x="294" y="58" width="7" height="82" fill="var(--blue)"/><rect x="301" y="31" width="7" height="109" fill="var(--orange)"/><rect x="308" y="66" width="7" height="74" fill="var(--grey-mid)"/><text x="296" y="148">2015</text></g>
        <rect x="190" y="153" width="3" height="3" fill="var(--blue)"/><text x="194" y="156">UK</text>
        <rect x="203" y="153" width="3" height="3" fill="var(--orange)"/><text x="207" y="156">USA</text>
        <rect x="218" y="153" width="3" height="3" fill="var(--grey-mid)"/><text x="222" y="156">France</text>
      </g>
    </svg>
    <svg class="frame" viewBox="0 0 440 330"><polygon points="0,299 150,320 440,298 440,330 0,330" fill="var(--blue)"/><polyline points="0,296 150,317 440,295" fill="none" stroke="#bbb"/></svg>
    <div class="page-no">3.</div><div class="url">www.tarnridgepartners.com</div>
  </section>

  <!-- 4 subtitles -->
  <section class="slide content" style="left:54px;top:873px;transform:scale(.8)">
    <h2 class="slide-head" style="top:12px">LOREM IPSUM</h2>
    <div class="subs">
      <div class="sub"><h3>Sub Title-1</h3><p>Lorem ipsum dolor sit amet, etuer.Lorem ipsum dolor sit amet, etuer.Lorem ipsum dolor sit amet, etuer.Lorem ipsum dolor</p></div>
      <div class="sub"><h3>Sub Title-1</h3><p>Lorem ipsum dolor sit amet, etuer.Lorem ipsum dolor sit amet, etuer.Lorem ipsum dolor sit amet, etuer.Lorem ipsum dolor</p></div>
      <div class="sub"><h3>Sub Title-2</h3><p>Lorem ipsum dolor sit amet, etuer.Lorem ipsum dolor sit amet, etuer.Lorem ipsum dolor sit amet, etuer.Lorem ipsum dolor</p></div>
      <div class="sub"><h3>Sub Title-2</h3><p>Lorem ipsum dolor sit amet, etuer.Lorem ipsum dolor sit amet, etuer.Lorem ipsum dolor sit amet, etuer.Lorem ipsum dolor</p></div>
      <div class="sub"><h3>Sub Title-3</h3><p>Lorem ipsum dolor sit amet, etuer.Lorem ipsum dolor sit amet, etuer.Lorem ipsum dolor sit amet, etuer.Lorem ipsum dolor</p></div>
      <div class="sub"><h3>Sub Title-3</h3><p>Lorem ipsum dolor sit amet, etuer.Lorem ipsum dolor sit amet, etuer.Lorem ipsum dolor sit amet, etuer.Lorem ipsum dolor</p></div>
    </div>
    <svg class="frame" viewBox="0 0 440 330"><polygon points="0,299 150,320 440,298 440,330 0,330" fill="var(--blue)"/><polyline points="0,296 150,317 440,295" fill="none" stroke="#bbb"/></svg>
    <div class="page-no">4.</div><div class="url">www.tarnridgepartners.com</div>
  </section>

  <!-- 5 hexagon infographic -->
  <section class="slide content" style="left:426px;top:871px;transform:scale(.8)">
    <h2 class="slide-head">LOREM IPSUM</h2>
    <svg class="frame" viewBox="0 0 440 330">
      <defs>
        <polygon id="hex" points="0,-33 29,-16.5 29,16.5 0,33 -29,16.5 -29,-16.5"/>
        <g id="ico-card"><rect x="-13" y="-9" width="26" height="18" rx="2" fill="#fff"/><rect x="-13" y="-4" width="26" height="4" fill="currentColor"/><rect x="-9" y="3" width="9" height="2" fill="currentColor"/></g>
        <g id="ico-bars"><rect x="-11" y="0" width="5" height="10" fill="#fff"/><rect x="-3" y="-6" width="5" height="16" fill="#fff"/><rect x="5" y="-12" width="5" height="22" fill="#fff"/><line x1="-14" y1="11" x2="13" y2="11" stroke="#fff" stroke-width="2"/></g>
        <g id="ico-bank"><polygon points="0,-13 14,-5 -14,-5" fill="#fff"/><rect x="-11" y="-3" width="4" height="12" fill="#fff"/><rect x="-2" y="-3" width="4" height="12" fill="#fff"/><rect x="7" y="-3" width="4" height="12" fill="#fff"/><rect x="-14" y="10" width="28" height="3" fill="#fff"/></g>
        <g id="ico-bag"><circle cx="0" cy="3" r="11" fill="#fff"/><polygon points="-5,-13 5,-13 2,-7 -2,-7" fill="#fff"/><text x="0" y="8" text-anchor="middle" font-size="14" font-weight="900" fill="currentColor" font-family="Lato,sans-serif">$</text></g>
        <g id="ico-gear"><rect x="-12" y="-12" width="24" height="24" rx="3" fill="none" stroke="#fff" stroke-width="2.5"/><circle cx="4" cy="-2" r="4" fill="none" stroke="#fff" stroke-width="2.5"/><line x1="-5" y1="-7" x2="-5" y2="7" stroke="#fff" stroke-width="2.5"/></g>
      </defs>
      <g color="var(--blue)"><use href="#hex" x="150" y="108" fill="var(--blue)"/><use href="#ico-bank" x="150" y="108"/></g>
      <g color="var(--grey)"><use href="#hex" x="220" y="108" fill="var(--grey)"/><use href="#ico-card" x="220" y="108"/></g>
      <g color="var(--blue)"><use href="#hex" x="290" y="108" fill="var(--blue)"/><use href="#ico-gear" x="290" y="108"/></g>
      <g color="var(--grey)"><use href="#hex" x="115" y="170" fill="var(--grey)"/><use href="#ico-bars" x="115" y="170"/></g>
      <g color="var(--blue)"><use href="#hex" x="185" y="170" fill="var(--blue)"/><use href="#ico-bag" x="185" y="170"/></g>
      <g color="var(--grey)"><use href="#hex" x="255" y="170" fill="var(--grey)"/><use href="#ico-bank" x="255" y="170"/></g>
      <g color="var(--blue)"><use href="#hex" x="325" y="170" fill="var(--blue)"/><use href="#ico-card" x="325" y="170"/></g>
      <g color="var(--blue)"><use href="#hex" x="150" y="232" fill="var(--blue)"/><use href="#ico-gear" x="150" y="232"/></g>
      <g color="var(--grey)"><use href="#hex" x="220" y="232" fill="var(--grey)"/><use href="#ico-bars" x="220" y="232"/></g>
      <g color="var(--blue)"><use href="#hex" x="290" y="232" fill="var(--blue)"/><use href="#ico-bag" x="290" y="232"/></g>
      <polygon points="0,299 150,320 440,298 440,330 0,330" fill="var(--blue)"/><polyline points="0,296 150,317 440,295" fill="none" stroke="#bbb"/>
    </svg>
    <div class="hex-label" style="left:48px;top:58px"><b>Lorem Ipsum</b>Lorem ipsum this is<br>lorem text.</div>
    <div class="hex-label muted" style="left:200px;top:42px"><b>Lorem Ipsum</b>Lorem ipsum this is<br>lorem text.</div>
    <div class="hex-label" style="left:362px;top:55px;text-align:right"><b>Lorem Ipsum</b>Lorem ipsum this is<br>lorem text.</div>
    <div class="hex-label muted" style="left:20px;top:130px"><b>Lorem Ipsum</b>Lorem ipsum this is<br>lorem text.</div>
    <div class="hex-label" style="left:362px;top:115px;text-align:right"><b>Lorem Ipsum</b>Lorem ipsum this is<br>lorem text.</div>
    <div class="hex-label" style="left:45px;top:206px"><b>Lorem Ipsum</b>Lorem ipsum this is<br>lorem text.</div>
    <div class="hex-label" style="left:362px;top:203px;text-align:right"><b>Lorem Ipsum</b>Lorem ipsum this is<br>lorem text.</div>
    <div class="hex-label" style="left:74px;top:264px"><b>Lorem Ipsum</b>Lorem ipsum this is<br>lorem text.</div>
    <div class="hex-label muted" style="left:193px;top:275px"><b>Lorem Ipsum</b>Lorem ipsum this is<br>lorem text.</div>
    <div class="hex-label muted" style="left:308px;top:270px"><b>Lorem Ipsum</b>Lorem ipsum this is<br>lorem text.</div>
    <div class="page-no">5.</div><div class="url">www.tarnridgepartners.com</div>
  </section>

  <!-- 6 closing -->
  <section class="slide closing" style="left:801px;top:873px;transform:scale(.8)">
    <div class="photo closing-photo" role="img" aria-label="Dark blurred photo of hands typing on a laptop"></div>
    <div class="brand">TARN RIDGE PARTNERS</div>
    <div class="brand-rule"></div>
    <div class="thanks">Thank You!<small>for watching!</small></div>
    <div class="contact" style="top:242px"><svg viewBox="0 0 10 10"><circle cx="5" cy="5" r="5" fill="#fff"/><circle cx="5" cy="4" r="1.6" fill="#333"/></svg>Street Name, City Name, Zipcode-12345</div>
    <div class="contact" style="top:256px"><svg viewBox="0 0 10 10"><path d="M2 1 L4 1 L5 3 L4 4 Q5 6 6 6 L7 5 L9 6 L9 8 Q5 9 1 3 Z" fill="#fff"/></svg>012-345-6789<svg viewBox="0 0 10 10"><rect x="0" y="2" width="10" height="7" fill="#fff"/><polyline points="0,2 5,6 10,2" fill="none" stroke="#333"/></svg>info@tarnridgepartners.com</div>
    <svg class="frame" viewBox="0 0 440 330"><polygon points="0,299 150,320 440,298 440,330 0,330" fill="var(--blue)"/><polyline points="0,296 150,317 440,295" fill="none" stroke="#999"/></svg>
    <div class="page-no">6.</div><div class="url" style="right:13px;bottom:8px">www.tarnridgepartners.com</div>
  </section>

</main>
</body>
</html>
```